New bussiness card, using company logo.
Lachlan Voss
Manager/Director
Birch Property Developments
Po Box 4657
Thuringowa Central
Qld
0455 386 218
lachlan@birchpropertydevelopments
eye catching, vibrant colours, professional

```html
<!DOCTYPE html>
<html lang="en">
<head>
<meta charset="utf-8">
<title>Birch Property Developments – Business Card</title>
<link rel="stylesheet" href="https://fonts.googleapis.com/css2?family=Open+Sans:wght@400;600;700;800&display=swap">
<style>
  :root {
    --backdrop-light: #8c8f93;
    --backdrop-dark: #4a4d51;
    --card-white: #ffffff;
    --brand-red: #e0232b;
    --brand-green: #6bb843;
    --green-light: #8fc63e;
    --green-deep: #5aae45;
    --ink: #222222;
    --ink-soft: #555555;
  }
  * { box-sizing: border-box; margin: 0; padding: 0; }
  html, body {
    width: 1200px;
    height: 726px;
    overflow: hidden;
  }
  body {
    position: relative;
    background: linear-gradient(90deg, var(--backdrop-dark), var(--backdrop-light) 35%, var(--backdrop-dark) 60%, var(--backdrop-light) 85%, var(--backdrop-dark));
    font-family: "Open Sans", Arial, sans-serif;
  }
  .card {
    position: absolute;
    overflow: hidden;
    box-shadow: 0 1px 3px rgba(0,0,0,.35);
  }
  .card--front { left: 42px; top: 36px; width: 546px; height: 312px; background: var(--card-white); }
  .card--back-white { left: 614px; top: 36px; width: 544px; height: 311px; background: var(--card-white); }
  .card--back-red { left: 42px; top: 376px; width: 546px; height: 310px; background: var(--brand-red); }
  .card--back-green { left: 613px; top: 376px; width: 545px; height: 312px; background: linear-gradient(120deg, var(--green-light), var(--green-deep)); }

  /* company name block (stands where the logo sits) */
  .company {
    position: absolute;
    display: flex;
    align-items: center;
    gap: 12px;
    white-space: nowrap;
    font-weight: 800;
    text-transform: uppercase;
    line-height: 1.08;
    letter-spacing: .5px;
  }
  .company--centered {
    left: 50%;
    transform: translateX(-50%);
    text-align: center;
  }
  .company__square {
    flex: none;
    width: 16px;
    height: 16px;
    background: var(--brand-green);
  }
  .card--front .company { left: 26px; top: 76px; font-size: 22px; color: var(--brand-red); }
  .card--back-white .company { top: 106px; font-size: 32px; color: var(--brand-red); }
  .card--back-white .company__square { width: 22px; height: 22px; }
  .card--back-red .company { top: 116px; font-size: 32px; color: var(--card-white); }
  .card--back-green .company { top: 120px; font-size: 28px; color: var(--card-white); }

  /* front side details */
  .accent-bar { position: absolute; width: 9px; border-radius: 4px; }
  .accent-bar--red { left: -4px; top: 179px; height: 121px; background: var(--brand-red); }
  .accent-bar--green { right: -4px; top: 229px; height: 56px; background: var(--brand-green); }

  .postal {
    position: absolute;
    left: 25px;
    top: 189px;
    font-size: 14px;
    line-height: 19px;
    color: var(--ink);
  }
  .contact-list {
    position: absolute;
    left: 25px;
    top: 242px;
    list-style: none;
    font-size: 14px;
    line-height: 21px;
    color: var(--ink);
  }
  .contact-list li { display: flex; align-items: center; gap: 6px; }
  .contact-list svg { width: 13px; height: 13px; flex: none; }

  .person {
    position: absolute;
    right: 16px;
    top: 236px;
    text-align: right;
  }
  .person__name { font-size: 20px; font-weight: 700; color: var(--brand-red); line-height: 26px; }
  .person__role { font-size: 16px; color: var(--ink-soft); line-height: 22px; }

  .website {
    position: absolute;
    left: 0;
    right: 0;
    text-align: center;
    font-size: 15px;
    font-weight: 600;
    letter-spacing: 1.2px;
  }
  .card--back-white .website { top: 269px; color: var(--ink); }
  .card--back-red .website { top: 268px; color: var(--card-white); }
  .card--back-green .website { top: 270px; color: var(--card-white); }
</style>
</head>
<body>

  <section class="card card--front" aria-label="Business card front">
    <div class="company"><span class="company__square"></span><span>Birch Property<br>Developments</span></div>

    <span class="accent-bar accent-bar--red"></span>
    <span class="accent-bar accent-bar--green"></span>

    <p class="postal">Po Box 4657<br>Thuringowa Central , Qld</p>

    <ul class="contact-list">
      <li>
        <svg viewBox="0 0 14 14" aria-hidden="true"><circle cx="7" cy="7" r="7" fill="var(--brand-green)"/><path d="M4.5 3.5l1.6 0 .6 2-1 .8c.5 1.1 1.3 1.9 2.4 2.4l.8-1 2 .6v1.6c-3.8.3-6.7-2.6-6.4-6.4z" fill="#fff"/></svg>
        0455 386 218
      </li>
      <li>
        <svg viewBox="0 0 14 14" aria-hidden="true"><rect x="0" y="3" width="14" height="9" rx="1.5" fill="var(--brand-green)"/><path d="M1 4l6 4.5L13 4" fill="none" stroke="#fff" stroke-width="1.3"/></svg>
        lachlan@birchpropertydevelopments.com
      </li>
    </ul>

    <div class="person">
      <p class="person__name">Lachlan Voss</p>
      <p class="person__role">Manager/Director</p>
    </div>
  </section>

  <section class="card card--back-white" aria-label="Business card back, white">
    <div class="company company--centered"><span class="company__square"></span><span>Birch Property<br>Developments</span></div>
    <p class="website">www.birchpropertydevelopments.com</p>
  </section>

  <section class="card card--back-red" aria-label="Business card back, red">
    <div class="company company--centered"><span>Birch Property<br>Developments</span></div>
    <p class="website">www.birchpropertydevelopments.com</p>
  </section>

  <section class="card card--back-green" aria-label="Business card back, green">
    <div class="company company--centered"><span>Birch Property<br>Developments</span></div>
    <p class="website">www.birchpropertydevelopments.com</p>
  </section>

</body>
</html>
```